Save the Date card

This will be a Save the Date 5x7 card...preferably Hunter Green background

Annual Fund Leadership Dinner
June 20, 2023. 6:30 pm
Location: The Pellworth's Home
4187 Brimlow Ridge Rd
Alderby, TN 37990

Other side of card:
We would prayerfully ask that you consider partnering with us as we kick off our Annual Fund this Fall to celebrate our 25 year anniversary as an Academy.
Please direct any questions to Marlene Tobbitt, our Director of Advancement 423-555-0176 x 3051 or advancement@fernwickca.org

```html
<!DOCTYPE html>
<html lang="en">
<head>
<meta charset="utf-8">
<title>Annual Fund Leadership Dinner – Save the Date</title>
<link href="https://fonts.googleapis.com/css2?family=Crimson+Pro:wght@600;700&family=Montserrat:wght@400;500;600;700&family=Great+Vibes&display=swap" rel="stylesheet">
<style>
  :root{
    --hunter:#1f3324;
    --gold:#a59a58;
    --gold-soft:#c9bf86;
    --paper:#eef0f0;
    --white:#ffffff;
    --stage:#d3d3d3;
  }
  html,body{margin:0;padding:0;overflow:hidden;}
  body{width:1200px;height:2216px;background:var(--stage);position:relative;}
  .card{position:absolute;left:126px;width:948px;height:675px;box-shadow:-8px 8px 14px rgba(0,0,0,.35);}
  .card--front{top:395px;}
  .card--back{top:1145px;}
  .card svg{display:block;}
  .serif{font-family:"Crimson Pro",Georgia,serif;font-weight:700;}
  .sans{font-family:"Montserrat",Arial,sans-serif;font-weight:500;}
  .script{font-family:"Great Vibes",cursive;}
</style>
</head>
<body>

<div class="card card--front">
<svg width="948" height="675" viewBox="0 0 948 675">
  <defs>
    <linearGradient id="paper-grad" x1="0" y1="0" x2="1" y2="1">
      <stop offset="0" stop-color="#e4e7e7"/>
      <stop offset="0.5" stop-color="#f6f7f7"/>
      <stop offset="1" stop-color="#e9ecec"/>
    </linearGradient>
    <linearGradient id="photo-grad" x1="0" y1="0" x2="0" y2="1">
      <stop offset="0" stop-color="#b8a994"/>
      <stop offset="0.45" stop-color="#8d7f6d"/>
      <stop offset="0.75" stop-color="#c7c2bb"/>
      <stop offset="1" stop-color="#eceeef"/>
    </linearGradient>
  </defs>

  <rect class="front-bg" width="948" height="675" fill="url(#paper-grad)"/>

  <path class="front-gold-edge" d="M0,432 Q300,560 640,460 L948,420 L948,675 L0,675 Z" fill="var(--gold)"/>
  <path class="front-green-band" d="M0,446 Q300,572 650,478 L948,432 L948,675 L0,675 Z" fill="var(--hunter)"/>

  <text class="serif school-mark" x="238" y="132" text-anchor="middle" font-size="78" fill="var(--hunter)">FCA</text>

  <text class="serif event-title" x="238" y="255" text-anchor="middle" font-size="56" fill="var(--hunter)">Annual Fund</text>
  <text class="serif event-title" x="238" y="313" text-anchor="middle" font-size="56" fill="var(--hunter)">Leadership Dinner</text>

  <path class="date-frame" d="M86,363 L67,363 L67,416 L180,416 M297,416 L408,416 L408,363 L392,363" fill="none" stroke="var(--gold)" stroke-width="2"/>
  <text class="serif event-date" x="238" y="382" text-anchor="middle" font-size="42">
    <tspan fill="var(--hunter)">June 20th </tspan><tspan fill="var(--gold)">2023</tspan>
  </text>
  <rect class="time-pill" x="180" y="397" width="117" height="39" rx="19.5" fill="var(--gold)"/>
  <text class="serif event-time" x="238.5" y="425" text-anchor="middle" font-size="28" font-weight="600" fill="var(--paper)">6:30 pm</text>

  <path class="photo-frame" d="M480,90 Q480,40 540,34 Q699,10 858,34 Q918,40 918,90 L918,420 Q918,560 699,650 Q480,560 480,420 Z" fill="var(--gold)"/>
  <path class="photo" role="img" aria-label="Photo of four guests in business attire chatting beside a catered buffet table" d="M496,96 Q496,55 550,50 Q699,28 848,50 Q902,55 902,96 L902,415 Q902,548 699,630 Q496,548 496,415 Z" fill="url(#photo-grad)" stroke="var(--white)" stroke-width="2"/>

  <rect class="location-tab" x="27" y="519" width="111" height="29" rx="3" fill="var(--paper)"/>
  <text class="sans location-label" x="82.5" y="541" text-anchor="middle" font-size="19" fill="var(--gold)">Location:</text>
  <line x1="138" y1="547" x2="471" y2="547" stroke="var(--paper)" stroke-width="1.5"/>
  <text class="sans address" font-size="21" fill="var(--white)">
    <tspan x="27" y="576">The Pellworth's Home 4187 Brimlow Ridge</tspan>
    <tspan x="27" y="601">Rd Alderby, TN 37990</tspan>
  </text>

  <rect class="web-pill" x="27" y="615" width="260" height="31" rx="15.5" fill="var(--white)"/>
  <circle cx="45" cy="630.5" r="8" fill="none" stroke="var(--gold)" stroke-width="2"/>
  <line x1="37" y1="630.5" x2="53" y2="630.5" stroke="var(--gold)" stroke-width="1.5"/>
  <text class="sans web" x="61" y="637" font-size="18" fill="var(--hunter)">www.fernwickca.org</text>
  <g class="social" fill="var(--white)" stroke="var(--gold)" stroke-width="2">
    <circle cx="312" cy="631" r="14"/>
    <circle cx="347" cy="631" r="14"/>
    <circle cx="384" cy="631" r="14"/>
    <circle cx="419" cy="631" r="14"/>
    <circle cx="456" cy="631" r="14"/>
  </g>
</svg>
</div>

<div class="card card--back">
<svg width="948" height="675" viewBox="0 0 948 675">
  <rect class="back-bg" width="948" height="675" fill="var(--hunter)"/>

  <text class="sans appeal" font-size="24" fill="var(--white)">
    <tspan x="83" y="133">We would prayerfully ask that you</tspan>
    <tspan x="83" y="163">consider partnering with us as we</tspan>
    <tspan x="83" y="193">kick off our Annual Fund this Fall</tspan>
    <tspan x="83" y="223">to celebrate our</tspan>
  </text>

  <text class="sans num-five" x="738" y="316" font-size="210" font-weight="700" fill="var(--gold)">5</text>
  <text class="sans num-two" x="588" y="204" font-size="165" font-weight="700" fill="var(--white)">2</text>
  <rect class="years-tag" x="712" y="120" width="69" height="26" fill="var(--gold)"/>
  <text class="sans years" x="746.5" y="140" text-anchor="middle" font-size="16" fill="var(--white)">YEARS</text>
  <text class="sans celebrating" x="545" y="230" font-size="17" font-weight="400" letter-spacing="5" fill="var(--gold-soft)">CELEBRATING</text>
  <text class="script anniversary" x="545" y="270" font-size="46" fill="var(--white)">anniversary</text>
  <line x1="545" y1="280" x2="725" y2="280" stroke="var(--white)" stroke-width="1.5"/>

  <path class="wave-white" d="M0,378 C200,300 420,420 600,450 C750,470 880,420 948,372 L948,675 L0,675 Z" fill="var(--white)"/>
  <path class="wave-gold" d="M0,396 C200,330 420,440 600,470 C750,492 880,446 948,396 L948,675 L0,675 Z" fill="var(--gold)"/>

  <text class="sans contact" font-size="24" fill="var(--white)">
    <tspan x="83" y="516">Please direct any questions to Marlene</tspan>
    <tspan x="83" y="546">Tobbitt, our Director of Advancement</tspan>
  </text>
  <path class="phone-icon" d="M88,567 q-4,2 -3,7 q3,10 12,16 q4,3 8,0 l2,-3 q1,-2 -1,-3 l-4,-3 q-2,-1 -3,1 l-1,1 q-5,-3 -7,-8 l1,-1 q2,-1 1,-3 l-2,-4 q-1,-2 -3,0 Z" fill="var(--white)"/>
  <text class="sans phone" x="120" y="596" font-size="30" fill="var(--white)">423-555-0176</text>

  <rect class="email-pill" x="83" y="606" width="301" height="31" rx="6" fill="var(--hunter)"/>
  <rect x="96" y="615" width="18" height="13" rx="1.5" fill="var(--white)"/>
  <path d="M96,616 L105,623 L114,616" fill="none" stroke="var(--hunter)" stroke-width="1.5"/>
  <text class="sans email" x="122" y="627" font-size="16" fill="var(--white)">advancement@fernwickca.org</text>

  <text class="serif school-mark" x="687" y="585" text-anchor="middle" font-size="78" fill="var(--white)">FCA</text>
</svg>
</div>

</body>
</html>
```